I need a business card design for a new company that will be doing consulting work around issues of cultural competency, and diversity and inclusion. I would like the design to be crisp and clear with bold but conservative colors and incorporate shades of blue

Target Market(s)

Small businesses, schools, non-profits

Industry/Entity Type

Consulting

Font styles to use
Serif
Sans Serif

Colors
0c5ba6
6b449b
3276b5
0292cd

Requirements
Must have
• A Morrow Venture (name of company)
• Lemlem Tavish
• CEO
• lemlem@amorrowventure.com
• (215)483-2756

```html
<!DOCTYPE html>
<html lang="en">
<head>
<meta charset="UTF-8">
<title>A Morrow Venture — Business Card</title>
<link rel="stylesheet" href="https://fonts.googleapis.com/css2?family=Roboto:wght@300;400;700&display=swap">
<style>
  :root {
    --brand-navy: #0c5ba6;
    --brand-deep: #0d4fa0;
    --brand-sky: #0292cd;
    --card-light: #ffffff;
    --card-edge: #e4e5e8;
    --text-on-blue: #ffffff;
    --icon-outline: #123a66;
  }
  html, body {
    margin: 0;
    padding: 0;
    width: 1200px;
    height: 1200px;
    overflow: hidden;
    background: #ffffff;
    font-family: "Roboto", Arial, sans-serif;
  }
  .canvas {
    position: relative;
    width: 1200px;
    height: 1200px;
  }
  .card {
    position: absolute;
    left: 181px;
    top: 360px;
    width: 838px;
    height: 480px;
    overflow: hidden;
  }
  .card-art {
    position: absolute;
    inset: 0;
    width: 100%;
    height: 100%;
  }
  .text {
    position: absolute;
    margin: 0;
    line-height: 1;
    white-space: nowrap;
  }
  .company {
    left: 216px;
    top: 391px;
    font-size: 53px;
    font-weight: 700;
    color: var(--text-on-blue);
    letter-spacing: -0.3px;
  }
  .person {
    left: 216px;
    top: 455px;
    font-size: 37px;
    font-weight: 400;
    color: var(--text-on-blue);
  }
  .role {
    left: 216px;
    top: 502px;
    font-size: 30px;
    font-weight: 300;
    color: var(--text-on-blue);
  }
  .contact {
    right: 306px;
    font-size: 34px;
    font-weight: 300;
    color: var(--brand-sky);
  }
  .phone { top: 697px; }
  .email { top: 753px; }
  .icon {
    position: absolute;
  }
  .icon-phone { left: 926px; top: 690px; width: 54px; height: 50px; }
  .icon-mail { left: 922px; top: 757px; width: 56px; height: 40px; }
</style>
</head>
<body>
<div class="canvas">
  <div class="card">
    <svg class="card-art" viewBox="0 0 1048 600" preserveAspectRatio="none" aria-hidden="true">
      <defs>
        <radialGradient id="cardGlow" cx="0.52" cy="0.68" r="0.75">
          <stop offset="0" stop-color="var(--card-light)"/>
          <stop offset="1" stop-color="var(--card-edge)"/>
        </radialGradient>
        <filter id="softShadow" x="-10%" y="-10%" width="120%" height="130%">
          <feDropShadow dx="0" dy="4" stdDeviation="3" flood-color="#000" flood-opacity="0.35"/>
        </filter>
      </defs>
      <rect class="card-ground" width="1048" height="600" fill="url(#cardGlow)"/>
      <path class="band-sky" filter="url(#softShadow)" fill="var(--brand-sky)"
            d="M1048,228 C820,320 420,345 0,300 L0,306 C400,372 820,352 1048,265 Z"/>
      <path class="band-deep" filter="url(#softShadow)" fill="var(--brand-deep)"
            d="M1048,158 C820,262 420,330 0,282 L0,290 C420,342 820,292 1048,172 Z"/>
      <path class="header-wave" filter="url(#softShadow)" fill="var(--brand-navy)"
            d="M0,0 H1048 C760,150 360,300 0,285 Z"/>
    </svg>

    <div></div>
  </div>

  <h1 class="text company">A Morrow Venture</h1>
  <p class="text person">Lemlem Tavish</p>
  <p class="text role">CEO</p>

  <p class="text contact phone">(215)483-2756</p>
  <p class="text contact email">lemlem@amorrowventure.com</p>

  <svg class="icon icon-phone" viewBox="0 0 54 50" aria-hidden="true">
    <path d="M8,3 C3,5 1,11 4,18 C10,32 22,43 36,47 C43,49 48,46 50,42 L43,34 C41,33 39,33 37,35 L34,38 C26,34 18,26 15,18 L18,15 C20,13 20,11 19,9 Z"
          fill="var(--brand-navy)" stroke="var(--icon-outline)" stroke-width="2" stroke-linejoin="round"/>
  </svg>
  <svg class="icon icon-mail" viewBox="0 0 56 40" aria-hidden="true">
    <rect x="2" y="2" width="52" height="36" fill="var(--brand-navy)" stroke="var(--icon-outline)" stroke-width="2"/>
    <rect x="6" y="6" width="44" height="28" fill="#ffffff"/>
    <path d="M6,6 L28,22 L50,6 M6,34 L22,18 M50,34 L34,18" fill="none" stroke="var(--icon-outline)" stroke-width="3"/>
  </svg>
</div>
</body>
</html>
```